Quillet Studios business card

Front of card should be logo and back of card should be communication info.
Please note: reverse the logo color. Card should be black and everything else white.

Industry/Entity Type

Custom home design/construction

Contact Information for Business Card

Quillet Studios, LLC 555-382-0146 quilletstudios@mailbox-example.com

Requirements
Must have
• Square card, Logo on front, communication info on back and perhaps a mini version of the logo on back also. Black card/white lettering. Double sides square card.
Nice to have
• I want to keep it simple. Our product (custom homes) speak for themselves.

```html
<!DOCTYPE html>
<html lang="en">
<head>
<meta charset="utf-8">
<title>Quillet Studios business card</title>
<link href="https://fonts.googleapis.com/css2?family=Comfortaa:wght@300;400&family=Lato:wght@400&family=Montserrat:wght@600;700&display=swap" rel="stylesheet">
<style>
  :root{
    --page:#ececec;
    --card:#0f0f0f;
    --text-light:#ffffff;
    --text-soft:#d9d9d9;
    --accent:#f6c38a;
    --accent-text:#f4b779;
    --icon-ink:#1e1e1e;
  }
  *{margin:0;padding:0;box-sizing:border-box}
  html,body{width:900px;height:1200px;overflow:hidden;background:var(--page)}
  .canvas{position:relative;width:900px;height:1200px}
  .card{position:absolute;left:190px;width:520px;height:520px;overflow:hidden;background:var(--card);box-shadow:0 8px 24px rgba(0,0,0,.25)}
  .card--front{top:40px}
  .card--back{top:620px}

  .corner{position:absolute;width:84px;height:84px}
  .corner--top-right{right:24px;top:24px;border-top:2px solid var(--text-light);border-right:2px solid var(--text-light)}
  .corner--bottom-left{left:24px;bottom:24px;border-bottom:2px solid var(--text-light);border-left:2px solid var(--text-light)}

  .house-illustration{position:absolute;left:153px;top:118px;width:213px;height:143px}
  .brand-name{position:absolute;left:0;width:100%;top:278px;text-align:center;
    font-family:'Montserrat',sans-serif;font-weight:700;font-size:33px;color:var(--text-light);letter-spacing:.5px}
  .brand-tagline{position:absolute;left:0;width:100%;top:322px;text-align:center;
    font-family:'Montserrat',sans-serif;font-weight:600;font-size:17px;color:var(--text-soft);letter-spacing:5px}

  .back-art{position:absolute;inset:0}
  .company-name{position:absolute;left:40px;top:108px;font-family:'Comfortaa',sans-serif;font-weight:300;
    font-size:30px;color:var(--text-light);letter-spacing:-0.5px;white-space:nowrap}
  .company-role{position:absolute;left:41px;top:150px;font-family:'Comfortaa',sans-serif;font-weight:300;
    font-size:21px;color:var(--accent-text)}
  .contact-list{position:absolute;left:41px;top:206px;list-style:none}
  .contact-item{display:flex;align-items:center;height:30px;margin-bottom:24px;white-space:nowrap;
    font-family:'Lato',sans-serif;font-size:17px;color:var(--text-light)}
  .contact-icon{width:30px;height:30px;border-radius:50%;background:var(--accent);margin-right:15px;
    display:flex;align-items:center;justify-content:center;flex:none}
  .contact-icon svg{width:16px;height:16px;fill:none;stroke:var(--icon-ink);stroke-width:1.6;stroke-linecap:round;stroke-linejoin:round}
</style>
</head>
<body>
<main class="canvas">
  <section class="card card--front">
    <div class="corner corner--top-right"></div>
    <div class="corner corner--bottom-left"></div>
    <svg class="house-illustration" role="img" aria-label="White line drawing of a two-storey custom home" viewBox="0 0 213 143">
      <defs><linearGradient id="houseTone" x1="0" y1="0" x2="0" y2="1"><stop offset="0" stop-color="#3a3a3a"/><stop offset="1" stop-color="#2a2a2a"/></linearGradient></defs>
      <rect width="213" height="143" fill="url(#houseTone)"/>
    </svg>
    <div class="brand-name">QUILLET STUDIOS</div>
    <div class="brand-tagline">CUSTOM HOME BUILDERS</div>
  </section>

  <section class="card card--back">
    <svg class="back-art" viewBox="0 0 520 520" preserveAspectRatio="none">
      <defs>
        <linearGradient id="shadedScene" x1="0" y1="0" x2="0" y2="1">
          <stop offset="0" stop-color="#1a1b17"/><stop offset=".7" stop-color="#121211"/><stop offset="1" stop-color="#1a1d16"/>
        </linearGradient>
        <linearGradient id="homeScene" x1="0" y1="0" x2="0" y2="1">
          <stop offset="0" stop-color="#6f9a45"/><stop offset=".35" stop-color="#8a8577"/><stop offset=".7" stop-color="#b9ab8c"/><stop offset="1" stop-color="#7cb342"/>
        </linearGradient>
      </defs>
      <rect width="520" height="520" fill="url(#shadedScene)" role="img" aria-label="Darkened garden and porch of a house"/>
      <path d="M440,0 C385,130 390,380 480,520 L520,520 L520,0 Z" fill="url(#homeScene)" role="img" aria-label="Photo of a beige Victorian house among trees with a lawn"/>
    </svg>
    <div class="company-name">Quillet Studios, LLC</div>
    <div class="company-role">Custom Home Builders</div>
    <ul class="contact-list">
      <li class="contact-item"><span class="contact-icon"><svg viewBox="0 0 16 16"><path d="M4 2l2 3-1.3 1.3a8 8 0 0 0 5 5L11 10l3 2-1 2.5C7 14 2 9 1.5 3z"/></svg></span>555-382-0146</li>
      <li class="contact-item"><span class="contact-icon"><svg viewBox="0 0 16 16"><path d="M2 8l6-5 6 5M4 7v7h8V7M7 14v-4h2v4"/></svg></span>42nd Avenue NY</li>
      <li class="contact-item"><span class="contact-icon"><svg viewBox="0 0 16 16"><rect x="2" y="4" width="12" height="9" rx="1"/><path d="M2 5l6 4 6-4"/></svg></span>quilletstudios@mailbox-example.com</li>
      <li class="contact-item"><span class="contact-icon"><svg viewBox="0 0 16 16"><circle cx="8" cy="8" r="6"/><path d="M2 8h12M8 2c-3 3-3 9 0 12M8 2c3 3 3 9 0 12"/></svg></span>www.quilletstudios-example.com</li>
    </ul>
  </section>
</main>
</body>
</html>
```